Business Card for Musician

The company is called Tolvik Music Entertainment and i am the director (Priya Hallorin) . I would like a logo made along with a list of services i provide :

Rock Pop and Jazz Covers music for Weddings , Birthdays , Pubs, Bars and Restaurants

I provide Solo/Duo and Bands for these functions.

Another aspect is i teach guitar and do music workshops and compose music for television.

I want to go for something different than a photo of a guitar or singer..i like the idea of soundwaves and an ear. or ripples of sound like a music note (as a drop of water) and the sound rippling out..another idea is something with lighting (music lights) with different colours lighting up the name Tolvik..however im open to any ideas. Thanks

Target Market(s)

General Public, Music Agents, Venue Owners. English Speaking..adults from 25-50

Industry/Entity Type

Business

Font styles to use
Sans Serif

Colors

Designer to choose colors to be used in the design.

Requirements
Must have
• All the points about what i do...
Nice to have
• Logo could emphasize the TOL in Tolvik...
Should not have
• Not too busy please...Simple but gets the message across. NOthing obvious like a photo of a musician playing.

```html
<!DOCTYPE html>
<html lang="en">
<head>
<meta charset="utf-8">
<title>Tolvik Music Entertainment – Business Card</title>
<link rel="stylesheet" href="https://fonts.googleapis.com/css2?family=Arimo:wght@400;700&family=Tinos:ital,wght@0,700;1,700&display=swap">
<style>
  :root {
    --sky: #b3c7e9;
    --glow: #f3ec6a;
    --glow-warm: #f0b07a;
    --brand: #5b2a22;
    --name: #1d676d;
    --role: #2a97a6;
    --band: #40a0ad;
    --ink: #333333;
  }
  * { margin: 0; padding: 0; box-sizing: border-box; }
  html, body { width: 1200px; height: 686px; overflow: hidden; background: var(--sky); }
  .card {
    position: relative;
    width: 1200px;
    height: 686px;
    background: var(--sky);
    overflow: hidden;
  }
  .energy-art {
    position: absolute;
    left: 250px;
    top: 0;
    width: 850px;
    height: 560px;
    background:
      radial-gradient(ellipse 38% 22% at 42% 12%, rgba(240,176,122,0.55), transparent 70%),
      radial-gradient(ellipse 55% 40% at 60% 35%, rgba(243,236,106,0.35), transparent 70%),
      radial-gradient(ellipse 30% 45% at 85% 70%, rgba(243,236,106,0.22), transparent 70%);
  }
  .brand {
    position: absolute;
    left: 0;
    right: 0;
    top: 90px;
    text-align: center;
    font-family: "Arimo", Arial, sans-serif;
    font-weight: 700;
    color: var(--brand);
  }
  .brand-name {
    display: block;
    font-size: 84px;
    line-height: 1;
    letter-spacing: 2px;
  }
  .brand-tagline {
    display: block;
    margin-top: 14px;
    font-size: 44px;
    line-height: 1;
    letter-spacing: 1px;
  }
  .person {
    position: absolute;
    left: 0;
    right: 0;
    top: 408px;
    text-align: center;
    font-family: "Tinos", "Times New Roman", serif;
  }
  .person-name {
    font-weight: 700;
    font-size: 42px;
    font-variant: small-caps;
    letter-spacing: 1px;
    color: var(--name);
    line-height: 1;
  }
  .person-role {
    font-style: italic;
    font-weight: 700;
    font-size: 34px;
    color: var(--role);
    line-height: 1.2;
  }
  .services-band {
    position: absolute;
    left: 0;
    top: 528px;
    width: 1200px;
    height: 158px;
  }
  .services-band svg { position: absolute; inset: 0; }
  .services {
    position: absolute;
    left: 0;
    right: 0;
    top: 38px;
    text-align: center;
    font-family: "Arimo", Arial, sans-serif;
    font-size: 26px;
    line-height: 34px;
    color: var(--ink);
  }
  .services-line { display: block; white-space: nowrap; }
</style>
</head>
<body>
  <div class="card">
    <div class="energy-art" role="img" aria-label="Glowing yellow and orange lightning streaks crossing the sky"></div>

    <div class="brand">
      <span class="brand-name">Tolvik</span>
      <span class="brand-tagline">Music Entertainment</span>
    </div>

    <div class="person">
      <div class="person-name">Priya Hallorin</div>
      <div class="person-role">Director</div>
    </div>

    <div class="services-band">
      <svg width="1200" height="158" viewBox="0 0 1200 158" aria-hidden="true">
        <path d="M0 14 C 250 -4, 520 -2, 760 8 S 1100 20, 1200 12 L 1200 158 L 0 158 Z" fill="var(--band)"/>
      </svg>
      <p class="services">
        <span class="services-line">Solo/Duo and Bands, Rock Pop and Jazz Covers for Weddings,</span>
        <span class="services-line">Birthdays, Pubs, Bars and Restaurants</span>
        <span class="services-line">Guitar Lessons, Music Workshops and Composing for Television</span>
      </p>
    </div>
  </div>
</body>
</html>
```